Swing Dance Themed Cleaning Company Website

We need a website designed for a cleaning company based in Portland, Oregon called Bellhop Sweep. We clean homes and commercial buildings, inside and out.

needs to be vintage and like the velvet marlow. Speakeasy 1920s feel.
needs to be classy.

Check out bellhopsweep.com We are not happy with the site currently.

please look at house finderly site for more content https://www.housefinderly.com/rated.BellhopSweepCleaning.48217065.html

Check out my videos on my ClipHarbor channel Bellhop Sweep

Target Market(s)

middle class and home owner

Industry/Entity Type

Cleaning Service

Number of Pages Required

3 page

Font styles to use
Other font styles liked:
• jazzrag

Colors

Designer to choose colors to be used in the design.

Requirements
Must have
• must be good on pc and mobile

```html
<!DOCTYPE html>
<html lang="en">
<head>
<meta charset="utf-8">
<title>Bellhop Sweep – Cleaning Services Portland</title>
<link href="https://fonts.googleapis.com/css2?family=Poiret+One&family=Open+Sans:wght@400;600;700&display=swap" rel="stylesheet">
<style>
:root{
  --yellow:#f6e500;
  --black:#0b0b0b;
  --coal:#161616;
  --panel:#1e1e1e;
  --card:#2a2a2a;
  --text:#e9e9e9;
  --muted:#a9a9a9;
  --deco:'Poiret One', cursive;
  --body:'Open Sans', sans-serif;
}
*{box-sizing:border-box;margin:0;padding:0}
html,body{width:1200px;height:3600px;overflow:hidden;background:var(--black);color:var(--text);font-family:var(--body)}
.page{position:relative;width:1200px;height:3600px}
section,header,footer{position:absolute;left:0;width:1200px}
.btn{display:inline-block;font-family:var(--body);font-weight:700;font-size:17px;border-radius:22px;padding:10px 34px;text-decoration:none}
.btn-yellow{background:var(--yellow);color:#111}
.btn-outline{border:2px solid var(--yellow);color:var(--yellow)}
.btn-dark{background:#111;color:var(--yellow)}
.deco{font-family:var(--deco);font-weight:400;letter-spacing:2px;text-transform:uppercase}

/* header */
.site-header{top:0;height:152px;background:#111}
.brand{position:absolute;left:100px;top:40px;display:flex;gap:12px;align-items:center}
.brand-square{width:28px;height:28px;background:var(--yellow)}
.brand-name{font-family:var(--body);font-weight:600;color:var(--yellow);font-size:28px;line-height:34px;white-space:nowrap}
.quote-btn{position:absolute;right:100px;top:38px;border:2px solid var(--yellow);color:#fff;border-radius:22px;padding:8px 24px;font-size:17px;font-weight:600}
.main-nav{position:absolute;right:96px;top:94px;display:flex;gap:52px;font-size:17px;font-weight:600}
.main-nav a{color:#fff;text-decoration:none;padding-bottom:10px}
.main-nav a.active{border-bottom:3px solid var(--yellow)}

/* hero */
.hero{top:152px;height:668px}
.hero-photo{position:absolute;inset:0;background:linear-gradient(180deg,#9a9c9c 0%,#c9cacb 40%,#6d6e6e 75%,#3b3b3b 100%)}
.hero-caption{position:absolute;top:300px;width:100%;text-align:center}
.hero-caption h1{font-size:46px;color:#fff;text-shadow:0 2px 6px rgba(0,0,0,.6)}
.hero-caption .btn{margin-top:24px}
.arrow{position:absolute;top:306px;width:44px;height:44px;border-radius:50%;background:rgba(0,0,0,.55)}
.arrow.left{left:40px}.arrow.right{right:40px;background:var(--yellow)}
.dots{position:absolute;top:838px;left:0;width:1200px;display:flex;justify-content:center;gap:8px}
.dots span{width:10px;height:10px;border-radius:50%;background:#555}
.dots span.on{background:var(--yellow)}

/* about */
.about{top:820px;height:580px;background:radial-gradient(circle at 30% 40%,#2b2b2b,#141414 75%)}
.about-text{position:absolute;left:120px;top:140px;width:500px}
.about-text h2{font-size:42px;color:#fff}
.about-text .lead{font-size:15px;margin-top:8px;color:#ddd}
.about-text h3{font-size:40px;color:#fff;margin-top:44px}
.about-text p{font-size:15px;line-height:23px;margin-top:14px;color:#ccc}
.about-actions{margin-top:40px;display:flex;gap:26px}
.about-art{position:absolute;left:720px;top:110px;width:320px;height:330px;border-radius:12px;background:radial-gradient(circle,#3a3a3a,#1d1d1d 70%)}

/* services */
.services{top:1400px;height:600px;background:var(--black)}
.section-title{text-align:center;font-size:38px;color:#fff}
.services .section-title{margin-top:116px}
.services .intro{width:760px;margin:18px auto 0;text-align:center;font-size:15px;line-height:22px;font-weight:600;color:#ddd}
.service-grid{position:absolute;top:262px;left:120px;display:flex;gap:20px}
.service{width:225px;text-align:center}
.service-photo{height:205px}
.service h4{font-size:20px;color:#fff;margin-top:22px}

/* packages */
.packages{top:2000px;height:660px;background:radial-gradient(circle at 50% 30%,#2a2a2a,#151515 80%)}
.packages .section-title{margin-top:70px}
.package-grid{position:absolute;top:170px;left:120px;display:flex;gap:30px}
.package{width:300px;height:410px;background:var(--card);border:1px solid #444;position:relative}
.package h5{background:var(--yellow);color:#111;font-family:var(--deco);font-size:20px;text-align:center;padding:16px 0;margin:26px 20px 0;text-transform:uppercase;font-weight:400}
.package ul{list-style:none;margin:26px 30px 0}
.package li{font-size:15px;font-weight:600;color:#eee;margin-bottom:13px;padding-left:16px;position:relative;line-height:20px}
.package li::before{content:"";position:absolute;left:0;top:7px;width:6px;height:6px;border-radius:50%;background:var(--yellow)}
.package .btn{position:absolute;bottom:26px;left:50%;transform:translateX(-50%);white-space:nowrap}

/* blog */
.blog{top:2660px;height:580px;background:var(--black)}
.blog .section-title{margin-top:30px}
.blog .sub{text-align:center;font-size:16px;font-weight:600;color:#ddd;margin-top:4px}
.blog-grid{position:absolute;top:120px;left:120px;display:flex;gap:15px}
.post{width:310px;background:var(--card)}
.post-photo{height:200px}
.post-body{padding:12px 16px 16px}
.post-meta{display:flex;justify-content:space-between;font-size:13px;color:#ccc;font-weight:600}
.post h6{font-size:16px;color:#fff;margin-top:10px}
.post p{font-size:13px;line-height:18px;color:#aaa;margin-top:6px}
.post .more{display:block;margin-top:12px;font-size:14px;font-weight:700;color:#fff}
.blog .view{position:absolute;top:520px;left:50%;transform:translateX(-50%)}

/* footer */
.site-footer{top:3240px;height:360px;background:#1a1a1a}
.foot-brand{position:absolute;left:100px;top:46px}
.foot-brand .brand{position:static}
.foot-brand p{width:240px;font-size:13px;line-height:19px;color:#bbb;margin-top:30px}
.foot-col{position:absolute;top:50px}
.foot-col h6{font-family:var(--deco);font-size:18px;color:#fff;font-weight:400;text-transform:uppercase;margin-bottom:22px}
.foot-col li{list-style:none;font-size:14px;color:#ccc;margin-bottom:10px}
.contact-form{display:grid;grid-template-columns:1fr 1fr;gap:8px;width:240px}
.contact-form span{background:#2c2c2c;border:1px solid #444;height:30px;font-size:12px;color:#999;padding:6px 8px}
.contact-form span.wide{grid-column:1/3;height:56px}
.contact-form .send{grid-column:2;justify-self:end;background:var(--yellow);color:#111;border:0;border-radius:14px;height:26px;padding:4px 16px;font-weight:700}
.copy{position:absolute;left:0;bottom:0;width:1200px;height:48px;border-top:1px solid #333;padding:0 100px;display:flex;justify-content:space-between;align-items:center;font-size:13px;color:#aaa}
.social{display:flex;gap:10px}
.social i{width:26px;height:26px;border-radius:50%;background:#ddd;display:block}
</style>
</head>
<body>
<div class="page">

<header class="site-header">
  <div class="brand">
    <div class="brand-square"></div>
    <div class="brand-name">Bellhop Sweep</div>
  </div>
  <a class="quote-btn">Get a Quote</a>
  <nav class="main-nav">
    <a class="active">Home</a><a>About us</a><a>Our Services</a><a>Blog</a><a>Contact us</a>
  </nav>
</header>

<section class="hero">
  <div class="hero-photo" role="img" aria-label="Bright, freshly cleaned living room with sofas and large windows"></div>
  <span class="arrow left"><svg width="44" height="44"><path d="M26 14 L18 22 L26 30" stroke="#fff" stroke-width="3" fill="none"/></svg></span>
  <span class="arrow right"><svg width="44" height="44"><path d="M18 14 L26 22 L18 30" stroke="#111" stroke-width="3" fill="none"/></svg></span>
  <div class="hero-caption">
    <h1 class="deco">Wide range of cleaning services</h1>
    <a class="btn btn-yellow">Read More</a>
  </div>
</section>
<div class="dots"><span></span><span class="on"></span><span></span></div>

<section class="about">
  <div class="about-text">
    <h2 class="deco">About us</h2>
    <div class="lead">Making the greater Portland area clean, one building at a time</div>
    <h3 class="deco">Good people, great service</h3>
    <p>Bellhop Sweep is a family owned professional cleaning business. We provide our years of cleaning experience to homes and businesses in and around Portland, Oregon.</p>
    <div class="about-actions"><a class="btn btn-outline">Read More</a><a class="btn btn-yellow">Get Started</a></div>
  </div>
  <div class="about-art" role="img" aria-label="Chalk-style sketch of a dancing cleaner with a mop"></div>
</section>

<section class="services">
  <h2 class="section-title deco">Our Services</h2>
  <p class="intro">We provide cleaning and janitorial services for one-time and recurring needs. While this isn't an exhaustive list of available services, these are certainly the most commonly requested:</p>
  <div class="service-grid">
    <div class="service"><div class="service-photo" role="img" aria-label="Janitor mopping with a wet floor sign" style="background:linear-gradient(160deg,#8a8a80,#c8b84a 60%,#5a5a55)"></div><h4 class="deco">Janitorial Services</h4></div>
    <div class="service"><div class="service-photo" role="img" aria-label="Housekeeper cleaning a bright room" style="background:linear-gradient(160deg,#b9c2c4,#6f8ea0 60%,#3d4a52)"></div><h4 class="deco">House Cleaning</h4></div>
    <div class="service"><div class="service-photo" role="img" aria-label="Maintenance work in an office" style="background:linear-gradient(160deg,#cfcfcf,#8c8f90 60%,#4b4d4e)"></div><h4 class="deco">Maintenance</h4></div>
    <div class="service"><div class="service-photo" role="img" aria-label="Event hall set for a banquet" style="background:linear-gradient(160deg,#d9d2c4,#9a8e7a 60%,#4f4639)"></div><h4 class="deco">Event Services</h4></div>
  </div>
</section>

<section class="packages">
  <h2 class="section-title deco">Bellhop Sweep</h2>
  <div class="package-grid">
    <div class="package">
      <h5>General House Keeping</h5>
      <ul><li>Floor to ceiling dusting</li><li>Cobweb removal</li><li>Kitchen Cleaning</li><li>Bathroom cleaning</li><li>Sweep, mop and vacuum floors</li></ul>
      <a class="btn btn-yellow">Get Started</a>
    </div>
    <div class="package">
      <h5>General House Keeping</h5>
      <ul><li>All general house keeping</li><li>Make your house "move in" ready</li><li>Refrigerator and oven cleaning</li><li>Window washing</li><li>Carpet cleaning</li></ul>
      <a class="btn btn-dark">Get Started</a>
    </div>
    <div class="package">
      <h5>General House Keeping</h5>
      <ul><li>Leaf blowing</li><li>Pressure washing</li><li>Window washing</li><li>Exterior house detail (removes moss, dirt, cobwebs etc)</li><li>Gutter cleaning</li></ul>
      <a class="btn btn-yellow">Get Started</a>
    </div>
  </div>
</section>

<section class="blog">
  <h2 class="section-title deco">Our Blog</h2>
  <div class="sub">Explore</div>
  <div class="blog-grid">
    <article class="post"><div class="post-photo" role="img" aria-label="Mop cleaning a wooden floor" style="background:linear-gradient(160deg,#d8d4cc,#a89a80 60%,#5c5040)"></div>
      <div class="post-body"><div class="post-meta"><span>July 01, 2018</span><span>20 &nbsp; 15</span></div><h6>Blog Post Title Is</h6><p>Lorem Ipsum is simply dummy text of the printing and typesetting.</p><span class="more">Continue..</span></div></article>
    <article class="post"><div class="post-photo" role="img" aria-label="Gloved hand wiping a surface" style="background:linear-gradient(160deg,#e8e0c8,#d9b23a 55%,#6a5a30)"></div>
      <div class="post-body"><div class="post-meta"><span>June 01, 2018</span><span>20 &nbsp; 15</span></div><h6>Blog Post Title Is</h6><p>Lorem Ipsum is simply dummy text of the printing and typesetting.</p><span class="more">Continue..</span></div></article>
    <article class="post"><div class="post-photo" role="img" aria-label="Cleaning crew working in a living room" style="background:linear-gradient(160deg,#cfcfcf,#8a8a8a 60%,#3f3f3f)"></div>
      <div class="post-body"><div class="post-meta"><span>June 01, 2018</span><span>20 &nbsp; 15</span></div><h6>Blog Post Title Is</h6><p>Lorem Ipsum is simply dummy text of the printing and typesetting.</p><span class="more">Continue..</span></div></article>
  </div>
  <a class="btn btn-yellow view">View More</a>
</section>

<footer class="site-footer">
  <div class="foot-brand">
    <div class="brand">
      <div class="brand-square"></div>
      <div class="brand-name">Bellhop Sweep</div>
    </div>
    <p>Lorem Ipsum is simply dummy text of the printing and typesetting industry. Lorem Ipsum has been the industry's standard dummy text.</p>
  </div>
  <div class="foot-col" style="left:480px"><h6>Quick Link</h6><ul><li>Home</li><li>About us</li><li>Our Services</li><li>Blog</li><li>Contact</li></ul></div>
  <div class="foot-col" style="left:640px"><h6>Address</h6><ul><li>418 SE Lindell Ave #22</li><li>Portland, OR 97214</li><li>971-555-0148</li><li>hello@bellhopsweep.com</li></ul></div>
  <div class="foot-col" style="left:850px"><h6>Quick Contact</h6>
    <div class="contact-form"><span>Name</span><span>Phone</span><span class="wide">Message</span><span class="send">Send</span></div>
  </div>
  <div class="copy"><span>Copyright © 2018 Bellhop Sweep. All Rights Reserved.</span><div class="social"><i></i><i></i><i></i><i></i><i></i></div></div>
</footer>

</div>
</body>
</html>
```